Plakat-Design für Gemeinschaftspraxis
Briefing
Ausgangssituation
Wir sind eine Gemeinschaftspraxis, die aus Ärzten und Physiotherapeuten besteht. Diese sollen unter einer gemeinsamen Marke präsentiert werden, dem sogenannten „Kelvaro“ (Farbcode Grün und Grau). Zusätzlich werden die Physiotherapeuten noch unter einer Marke zusammengefasst, dem sogenannten „Tesmunda“ (Farbcode Blau und Grün).
Kelvaro und Tesmunda haben jeweils eigene Internetseiten, Flyer und auch Visitenkarten.
Da jedoch beide Marken am selben Standort tätig sind, sollen auf diversen Plakaten (die im Umfeld der Ordination hängen werden) und den Schildern an der Türe auch beide Marken gemeinsam präsentiert werden.
Logos inkl. Farbrichtlinien wurden bereits gestaltet. Als Designvorlage dient ebenso ein allgemeiner Flyer über „Kelvaro“ (s. Anhang).
Im Anhang an das Briefing finden Sie alle relevanten Dateien wie Logos, Farbcodes, Fotos etc., die Sie zur Gestaltung der Werbemittel benötigen. Die grafische Umsetzung, Gliederung etc. überlassen wir Ihnen und freuen uns auf übersichtliche Vorschläge. Es wäre schön, wenn sich die Farbcodes der jeweiligen Marken auch in den Werbemitteln widerspiegeln. Wichtig ist uns, dass die Werbemittel klar und gut strukturiert gestaltet sind und nicht überladen wirken.
Hier finden Sie all mögliche Logo-Dateien, den bestehenden Flyer, die Farbwerte ,...
https://filedrop-example.net/t-Xq4bnLzPae
Farbregeln:
Wenn im Werbemittel nur ein Logo vorkommt, dann ist die Farbregel wie folgt:
Farbcode Kelvaro: Grün und Grau
Farbcode Tesmunda: Blau und Grün
Wenn im Werbemittel beide Logos vorkommen, dann ist die Farbregel wie folgt:
Farbcode Kelvaro: bleibt Grün und Grau
Farbcode Tesmunda: wird geändert in Blau und Grau
Viele der Werbemittel werden bei plakatfix.at produziert. Wenn Sie den jeweiligen Link beim Punkt „Datenaufbereitung“ anklicken, können Sie falls nötig auch direkt Formatvorlagen in diver..
Aufgabenstellung
Dieser Auftrag umfasst die Gestaltung von vier Plakaten in div. Größen mit identem Inhalt.
Bitte gestallten Sie zu Beginn nur die Größe 4000x1500cm
Sobald sich das Design in die richtige Richtung entwickelt, können dann auch die anderen Größen angelegt werden.
--> Bei zufriedenstellender Arbeit stehen eine Reihe von Folgeaufträgen an. (Siehe unten)
Plakate (4 Stück)
1. Plakat
Größe: 4000x1500cm
Info: Hängt zur Bewerbung der Praxis im Außenbereich an diversen Standorten in den umliegenden Orten, auf einer Höhe von ca. 3 Metern und soll vor allem vorbeifahrende Autofahrer ansprechen.
Inhalt:
Die Logos Kelvaro und Tesmunda
Die Adresse: Lindenhofweg 17/3, 2397 Wiesenau
E-Mailadressen office@kelvaro.net und office@tesmunda.at
Websites: www.kelvaro.net und www.tesmunda.at
Text: „Gemeinschaftspraxis für Orthopädie und Physiotherapie“
Fachbereiche/Schlagwörter: Unfallchirurgie, Sportmedizin, Rehabilitation, Sportphysiotherapie
Weitere optionale Schlagworte: Chiropraktik, Akupunktur, Prävention, Massagen
Datenaufbereitung:
Druckformat: 4060x1560mm
Sicherheitsabstand: 40mm
Abstand vom Ösenmittelpunkt zum Rand: 15mm
Abstand der Ösen zueinander: ca 500mm
Ösendurchmesser: 15mm
https://www.plakatfix.at/produkte/banner-transparente/transparente-planen-banner/
2. Plakat
Größe: 3000x1000mm
Inhalt/Info: identisch zu Plakat Nr. 1 4000x1500, nur das Format ist anders.
Druckformat: 3060x1060mm
3. Plakat
Größe: 4000x850mm
Info: Hängt auf der Fassade unseres Gebäudes und soll den Standort der Ordination klar kennzeichnen. Soll vorbeifahrende Autofahrer und Fußgänger auf die Ordinat..

```html
<!DOCTYPE html>
<html lang="de">
<head>
<meta charset="utf-8">
<title>Kelvaro · Tesmunda – Gemeinschaftspraxis</title>
<link rel="stylesheet" href="https://fonts.googleapis.com/css2?family=Montserrat:wght@400;700;800&display=swap">
<style>
  :root {
    --brand-green: #76b82a;
    --brand-blue: #0b6fbd;
    --paper: #f4f4f4;
    --white: #ffffff;
  }
  html, body {
    margin: 0;
    padding: 0;
    width: 1200px;
    height: 461px;
    overflow: hidden;
    background: var(--paper);
  }
  .banner {
    display: block;
    width: 1200px;
    height: 461px;
    font-family: "Montserrat", sans-serif;
  }
  .deco-ring-green { fill: none; stroke: var(--brand-green); stroke-width: 1.2; }
  .deco-ring-blue { fill: none; stroke: var(--brand-blue); stroke-width: 1.2; }
  .band-blue { fill: var(--brand-blue); }
  .band-green { fill: var(--brand-green); }
  .headline-light { fill: var(--white); font-weight: 400; font-size: 37px; }
  .headline-bold { fill: var(--white); font-weight: 800; font-size: 36px; }
  .brand-kelvaro { fill: var(--brand-green); font-weight: 800; font-size: 21px; letter-spacing: 1px; }
  .brand-tesmunda { fill: var(--brand-blue); font-weight: 800; font-size: 21px; letter-spacing: 1px; }
  .brand-dot-green { fill: var(--brand-green); }
  .brand-dot-blue { fill: var(--brand-blue); }
  .keyword { fill: var(--white); font-weight: 700; font-size: 18px; }
  .address-light { fill: var(--white); font-weight: 400; font-size: 19px; }
  .address-bold { fill: var(--white); font-weight: 700; font-size: 19px; }
  .web-links { fill: var(--white); font-weight: 700; font-size: 21px; }
  .photo-ring-blue { fill: none; stroke: var(--brand-blue); stroke-width: 2; }
  .photo-ring-green { fill: none; stroke: var(--brand-green); stroke-width: 2; }
</style>
</head>
<body>
<svg class="banner" viewBox="0 0 1200 461" xmlns="http://www.w3.org/2000/svg">
  <defs>
    <linearGradient id="fill-massage" x1="0" y1="0" x2="1" y2="1">
      <stop offset="0" stop-color="#e9ecef"/>
      <stop offset="0.45" stop-color="#2f6fb8"/>
      <stop offset="0.75" stop-color="#d7a98a"/>
      <stop offset="1" stop-color="#b8cf3a"/>
    </linearGradient>
    <linearGradient id="fill-consult" x1="0" y1="0" x2="0" y2="1">
      <stop offset="0" stop-color="#eef0f2"/>
      <stop offset="0.6" stop-color="#8fb9d8"/>
      <stop offset="1" stop-color="#4a4f57"/>
    </linearGradient>
    <linearGradient id="fill-training" x1="0" y1="0" x2="1" y2="0">
      <stop offset="0" stop-color="#c78a9a"/>
      <stop offset="0.5" stop-color="#ece8e4"/>
      <stop offset="1" stop-color="#8d9096"/>
    </linearGradient>
    <clipPath id="clip-massage"><circle cx="825" cy="160" r="168"/></clipPath>
    <clipPath id="clip-consult"><circle cx="672" cy="336" r="86"/></clipPath>
    <clipPath id="clip-training"><circle cx="1098" cy="338" r="142"/></clipPath>
  </defs>

  <g class="decor">
    <circle class="deco-ring-green" cx="40" cy="150" r="86"/>
    <circle class="deco-ring-green" cx="636" cy="39" r="57"/>
    <circle class="deco-ring-blue" cx="0" cy="384" r="60"/>
    <circle class="deco-ring-green" cx="24" cy="456" r="75"/>
    <circle class="deco-ring-green" cx="1008" cy="444" r="54"/>
  </g>

  <g class="brands">
    <circle class="brand-dot-green" cx="274" cy="44" r="23"/>
    <text class="brand-kelvaro" x="178" y="80">KELVARO</text>
    <circle class="brand-dot-blue" cx="428" cy="44" r="23"/>
    <text class="brand-tesmunda" x="324" y="80">TESMUNDA</text>
  </g>

  <g class="headline">
    <rect class="band-blue" x="0" y="110" width="660" height="52"/>
    <text class="headline-light" x="330" y="154" text-anchor="middle">GEMEINSCHAFTSPRAXIS FÜR</text>
    <rect class="band-green" x="0" y="175" width="668" height="52"/>
    <text class="headline-bold" x="330" y="215" text-anchor="middle">ORTHOPÄDIE UND</text>
    <rect class="band-blue" x="0" y="239" width="676" height="52"/>
    <text class="headline-bold" x="330" y="278" text-anchor="middle">PHYSIOTHERAPIE</text>
  </g>

  <g class="photo photo-massage" role="img" aria-label="Foto: Physiotherapeut massiert den Rücken eines Patienten auf der Behandlungsliege">
    <rect x="650" y="-10" width="350" height="350" fill="url(#fill-massage)" clip-path="url(#clip-massage)"/>
    <circle class="photo-ring-blue" cx="825" cy="160" r="174"/>
  </g>
  <g class="photo photo-consult" role="img" aria-label="Foto: Beratungsgespräch zwischen Patient und Therapeutin am Tisch">
    <rect x="580" y="245" width="185" height="185" fill="url(#fill-consult)" clip-path="url(#clip-consult)"/>
    <circle class="photo-ring-green" cx="672" cy="336" r="91"/>
  </g>
  <g class="photo photo-training" role="img" aria-label="Foto: Patientin trainiert mit Schlingentrainer unter Anleitung eines Therapeuten">
    <rect x="950" y="190" width="300" height="300" fill="url(#fill-training)" clip-path="url(#clip-training)"/>
    <circle class="photo-ring-blue" cx="1098" cy="338" r="148"/>
  </g>

  <g class="specialties">
    <polygon class="band-green" points="966,42 1200,42 1200,67 948,67"/>
    <text class="keyword" x="1170" y="61" text-anchor="end">UNFALLCHIRURGIE</text>
    <polygon class="band-blue" points="990,72 1200,72 1200,97 1008,97"/>
    <text class="keyword" x="1170" y="91" text-anchor="end">SPORTMEDIZIN</text>
    <polygon class="band-green" points="1008,103 1200,103 1200,127 990,127"/>
    <text class="keyword" x="1170" y="121" text-anchor="end">REHABILITATION</text>
    <polygon class="band-blue" points="909,133 1200,133 1200,157 927,157"/>
    <text class="keyword" x="1170" y="152" text-anchor="end">SPORTPHYSIOTHERAPIE</text>
  </g>

  <g class="address">
    <polygon class="band-blue" points="0,376 570,376 556,404 0,404"/>
    <text x="66" y="398"><tspan class="address-light">LINDENHOFWEG 17/3 </tspan><tspan class="address-bold">2397 WIESENAU</tspan></text>
  </g>

  <g class="web">
    <polygon class="band-green" points="546,411 984,411 984,436 532,436"/>
    <text class="web-links" x="762" y="431" text-anchor="middle">KELVARO.AT · TESMUNDA.AT</text>
  </g>
</svg>
</body>
</html>
```